依頼詳細
人形町だけではなく、銀座でも配布予定のため、少しの高級感と親しみやすさを併せ持つようなデザインを希望いたします。
また、ローストチキンを思わず、注文したくなるようなチラシを作成していただきたいです。
記載項目
https://pagenoa.com/landing_pages/view/xq7m4
サイズ
A6
ページ数
片面
希望イメージ
シンプル 複雑
単色 カラフル
暗い 明るい
日常 高級
遊び心 厳粛
未来的 伝統的
女性的 男性的
希望する色
青系
納品ファイル
• 高解像度JPG (.jpg)
• イラストレーター形式 (.ai)
• フォトショップ形式 (.psd)
• PNG形式 (.png)
補足説明
店舗URL:https://www.lune-toki.com/

当方の想定していたイメージに最も合ったデザインを作成いただけました。

この度はご提案いただきありがとうございました。
当方の想定していたイメージに最も合ったデザインを作成いただけましたので、こちらを採用させていただきました。
また今後も機会がありましたらよろしくお願いいたします。
ありがとうございました。

```html
<!DOCTYPE html>
<html lang="ja">
<head>
<meta charset="utf-8">
<title>Xmas2019 LUNE ローストチキン</title>
<link rel="stylesheet" href="https://fonts.googleapis.com/css2?family=Noto+Serif+JP:wght@500;700;900&family=Noto+Sans+JP:wght@500;700;900&family=Playfair+Display:wght@700;900&display=swap">
<style>
:root{
  --red-deep:#7a0c10;
  --red:#a3151b;
  --red-bright:#c8202a;
  --gold:#d9b25a;
  --gold-light:#f3dc9a;
  --cream:#fbf3e2;
  --white:#ffffff;
}
*{margin:0;padding:0;box-sizing:border-box}
html,body{width:847px;height:1200px;overflow:hidden;background:var(--red-deep)}
.flyer{position:relative;width:847px;height:1200px;overflow:hidden;
  background:radial-gradient(ellipse at 50% 45%,var(--red-bright) 0%,var(--red) 45%,var(--red-deep) 100%);
  font-family:"Noto Serif JP",serif;color:var(--white)}
.period{position:absolute;top:14px;width:150px;height:150px;border-radius:50%;background:var(--cream);
  color:var(--red);text-align:center;display:flex;flex-direction:column;justify-content:center;align-items:center;
  font-family:"Noto Sans JP",sans-serif;font-weight:900;border:4px solid var(--gold);z-index:2}
.period--reserve{left:14px}
.period--sale{right:14px}
.period__label{background:var(--red);color:var(--white);font-size:17px;padding:1px 10px;border-radius:4px;margin-bottom:2px}
.period__year{font-size:14px;line-height:1.1}
.period__dates{font-size:21px;line-height:1.15;white-space:nowrap;letter-spacing:-1px}
.title{position:absolute;top:8px;left:0;width:100%;text-align:center;z-index:1}
.title__xmas{font-family:"Playfair Display",serif;font-weight:900;font-size:40px;line-height:1.1;color:var(--gold-light);letter-spacing:2px}
.title__shop{font-family:"Playfair Display",serif;font-weight:900;font-size:84px;line-height:.95;color:var(--white);letter-spacing:4px;text-shadow:0 3px 0 var(--red-deep)}
.title__dish{font-family:"Noto Serif JP",serif;font-weight:900;font-size:88px;line-height:1.05;color:var(--white);letter-spacing:2px;text-shadow:0 4px 0 var(--red-deep)}
.tagline{position:absolute;top:206px;width:100%;text-align:center;font-size:22px;font-weight:700;color:var(--gold-light);z-index:1}
.photo{position:absolute;top:236px;left:50px;width:747px;height:350px;border-radius:50%;
  background:radial-gradient(ellipse at 45% 40%,#f0c06a 0%,#c9853a 45%,#8a4a1c 80%,rgba(122,12,16,0) 100%)}
.price{position:absolute;top:498px;left:190px;font-family:"Playfair Display",serif;font-weight:900;font-size:118px;line-height:1;
  color:var(--gold-light);-webkit-text-stroke:3px var(--red-deep);text-shadow:0 5px 0 var(--red-deep);white-space:nowrap}
.price__yen{font-family:"Noto Serif JP",serif;font-size:52px}
.price__tax{font-family:"Noto Sans JP",sans-serif;font-size:18px;-webkit-text-stroke:0;color:var(--white)}
.limit{position:absolute;top:528px;left:620px;width:84px;height:84px;border-radius:50%;background:var(--white);color:var(--red);
  display:flex;align-items:center;justify-content:center;text-align:center;font-family:"Noto Sans JP",sans-serif;font-weight:900;font-size:18px;line-height:1.15}
.pickup{position:absolute;top:610px;left:0;width:100%;text-align:center;font-family:"Noto Sans JP",sans-serif;font-weight:700;font-size:19px;line-height:1.45}
.pickup__time{color:var(--gold-light);font-size:24px}
.story{position:absolute;top:676px;left:60px;width:727px;text-align:center;font-size:15px;line-height:1.6;font-weight:500}
.sets-lead{position:absolute;top:822px;width:100%;text-align:center}
.sets-lead__head{display:inline-flex;align-items:center;gap:12px;font-family:"Noto Sans JP",sans-serif;font-weight:900;font-size:26px;color:var(--white)}
.sets-lead__head::before,.sets-lead__head::after{content:"";width:40px;height:2px;background:var(--gold)}
.sets-lead__sub{font-size:16px;margin-top:4px}
.sets{position:absolute;top:900px;left:40px;width:767px;display:flex;gap:20px}
.set{flex:1;background:var(--cream);color:var(--red);border-radius:10px;padding:8px 10px 10px;text-align:center;font-family:"Noto Sans JP",sans-serif;font-weight:900}
.set__name{background:var(--red);color:var(--white);border-radius:5px;font-size:19px;padding:3px 0}
.set__price{font-size:52px;line-height:1.15}
.set__price small{font-size:18px}
.inquiry{position:absolute;top:1052px;width:100%;text-align:center;font-size:26px;font-weight:700}
.contact{position:absolute;top:1108px;left:50px;width:747px;display:flex;justify-content:space-between;align-items:center;
  font-family:"Playfair Display",serif;font-weight:700;font-size:40px}
.contact__tel{display:flex;align-items:center;gap:8px;font-family:"Noto Sans JP",sans-serif;font-weight:700;font-size:42px}
.contact__tel svg{width:34px;height:34px}
</style>
</head>
<body>
<main class="flyer">
  <div class="photo" role="img" aria-label="こんがり焼き上がった丸ごとのローストチキンの写真"></div>

  <div class="period period--reserve">
    <span class="period__label">予約期間</span>
    <span class="period__year">2019</span>
    <span class="period__dates">11/10(日)~<br>12/15(日)まで</span>
  </div>
  <div class="period period--sale">
    <span class="period__label">販売期間</span>
    <span class="period__year">2019</span>
    <span class="period__dates">12/20(金)~<br>25(水)まで</span>
  </div>

  <header class="title">
    <div class="title__xmas">Xmas2019</div>
    <div class="title__shop">LUNE</div>
    <div class="title__dish">ローストチキン</div>
  </header>

  <p class="tagline">トリュフ香るきのこのバターライスとともに</p>

  <div class="price">4,000<span class="price__yen">円</span><span class="price__tax">(税別)</span></div>
  <div class="limit">1日30羽<br>限定</div>

  <div class="pickup">
    <div class="pickup__time">受け取り時間：17:00 または 18:00</div>
    <div>受け取り店舗：ビストロ LUNE（人形町）or メゾン・ソレイユ（東銀座）</div>
  </div>

  <p class="story">グルメガイド星付きのフレンチレストラン出身のシェフが作るローストチキンを食べて、<br>贅沢なクリスマスのひと時を過ごしませんか？<br>中にはトリュフ香るきのこのバターライスがたっぷり。<br>しっとりジューシーで、ローストチキンってこんなに美味しいの？！と思える逸品です。<br>取りに来ていただく時間に合わせて、熱々できたてをご提供します！</p>

  <div class="sets-lead">
    <div class="sets-lead__head">チキンに加え、いつもよりもっと特別な日にしたい方へ</div>
    <div class="sets-lead__sub">下記のセットもご用意しております。</div>
  </div>

  <div class="sets">
    <div class="set">
      <div class="set__name">オードブルセット（全4品）</div>
      <div class="set__price">+2,000<small>円(税別)</small></div>
    </div>
    <div class="set">
      <div class="set__name">選べる1ボトルセット（泡、白、赤）</div>
      <div class="set__price">+8,000<small>円(税別)</small></div>
    </div>
  </div>

  <p class="inquiry">詳細は店舗にお問い合わせください。</p>

  <div class="contact">
    <span class="contact__name">Bistro LUNE</span>
    <span class="contact__tel">
      <svg viewBox="0 0 24 24" aria-hidden="true"><path fill="#ffffff" d="M6.6 10.8a15.1 15.1 0 0 0 6.6 6.6l2.2-2.2c.3-.3.7-.4 1-.2 1.1.4 2.3.6 3.6.6.6 0 1 .4 1 1V20c0 .6-.4 1-1 1A17 17 0 0 1 3 4c0-.6.4-1 1-1h3.5c.6 0 1 .4 1 1 0 1.3.2 2.5.6 3.6.1.3 0 .7-.2 1z"/></svg>
      03-5550-0142
    </span>
  </div>
</main>
</body>
</html>
```